Book Cover Quieting Gnats, Shouldn'ts and Maybes, Climbing out of the valley of sorrow

Need a book cover design for my new web site..Drpeterwalsby.com (website under construction) I'm appearing on Echo of Meridia radio show and want to add a cover design of my book.

My book with enpower people to break the chain of limiting beliefs and unlock their true potential so they will finally experience the life of their dreams

Radio

```html
<!DOCTYPE html>
<html lang="en">
<head>
<meta charset="utf-8">
<title>Quieting Gnats, Shouldn'ts and Maybes — Book Cover</title>
<link rel="stylesheet" href="https://fonts.googleapis.com/css2?family=Cinzel:wght@400;500&family=Libre+Caslon+Text:ital@0;1&display=swap">
<style>
  :root {
    --parchment-light: #a9824f;
    --parchment-mid: #7e5a33;
    --parchment-dark: #3f2a17;
    --navy: #1e2535;
    --navy-deep: #171d2b;
    --frame-brown: #6a4a34;
    --band-red: #8a2a2b;
    --band-red-dark: #6e1f21;
    --rule-red: #7d2426;
    --ink-white: #f5f1ea;
    --author-tan: #a08c6c;
  }
  html, body {
    margin: 0;
    padding: 0;
    width: 800px;
    height: 1200px;
    overflow: hidden;
    background: var(--parchment-dark);
  }
  .cover {
    position: relative;
    width: 800px;
    height: 1200px;
    overflow: hidden;
  }
  .cover__texture {
    position: absolute;
    inset: 0;
    background:
      radial-gradient(ellipse at 50% 45%, var(--parchment-light) 0%, var(--parchment-mid) 55%, var(--parchment-dark) 100%);
  }
  .panel {
    position: absolute;
    left: 73px;
    top: 213px;
    width: 654px;
    height: 780px;
    background: linear-gradient(180deg, var(--navy) 0%, var(--navy-deep) 100%);
    box-shadow: 0 6px 24px rgba(0,0,0,0.45);
  }
  .panel__frame {
    position: absolute;
    left: 23px;
    top: 23px;
    right: 23px;
    bottom: 22px;
    border: 10px solid var(--frame-brown);
  }
  .author {
    position: absolute;
    top: 270px;
    left: 73px;
    width: 654px;
    text-align: center;
    font-family: "Libre Caslon Text", serif;
    font-size: 15px;
    color: var(--author-tan);
    margin: 0;
  }
  .title-band {
    position: absolute;
    left: 0;
    top: 363px;
    width: 773px;
    height: 128px;
    background: linear-gradient(180deg, var(--band-red) 0%, var(--band-red-dark) 100%);
    box-shadow: 0 4px 12px rgba(0,0,0,0.35);
    display: flex;
    align-items: center;
    justify-content: center;
  }
  .title-band__word {
    font-family: "Cinzel", serif;
    font-weight: 500;
    font-size: 74px;
    letter-spacing: 1px;
    color: var(--ink-white);
    margin: 0;
    padding-left: 10px;
    text-shadow: 0 2px 3px rgba(0,0,0,0.4);
  }
  .title {
    position: absolute;
    top: 518px;
    left: 73px;
    width: 654px;
    margin: 0;
    text-align: center;
    font-family: "Libre Caslon Text", serif;
    font-weight: 400;
    font-size: 66px;
    line-height: 88px;
    color: var(--ink-white);
    text-shadow: 0 2px 4px rgba(0,0,0,0.5);
  }
  .title span { display: block; }
  .rule {
    position: absolute;
    left: 215px;
    width: 370px;
    height: 2px;
    background: linear-gradient(90deg, transparent 0%, var(--rule-red) 25%, var(--rule-red) 75%, transparent 100%);
  }
  .rule--top { top: 747px; }
  .rule--bottom { top: 886px; }
  .subtitle {
    position: absolute;
    top: 770px;
    left: 73px;
    width: 654px;
    margin: 0;
    text-align: center;
    font-family: "Libre Caslon Text", serif;
    font-style: italic;
    font-size: 32px;
    line-height: 46px;
    color: var(--ink-white);
  }
  .subtitle span { display: block; }
</style>
</head>
<body>
  <main class="cover">
    <div class="cover__texture" role="img" aria-label="Aged parchment background with faint handwritten script of the book title"></div>

    <div class="panel">
      <div class="panel__frame"></div>
    </div>

    <p class="author">Dr. Peter Walsby M.D.</p>

    <div class="title-band">
      <p class="title-band__word">QUIETING</p>
    </div>

    <h1 class="title">
      <span>Gnats, Shouldn'ts</span>
      <span>and Maybes</span>
    </h1>

    <div class="rule rule--top"></div>
    <p class="subtitle">
      <span>Climbing Out of the</span>
      <span>Valley of Sorrow</span>
    </p>
    <div class="rule rule--bottom"></div>
  </main>
</body>
</html>
```